Hallvard
Veneer Technology
Hallvard - Agriculture
Creative Brief
Agriculture
http://hallvard-veneertechnology.example
We have 4 different product lines.
1. Stone-Veneer
2.Sonic-Paneltrim
3.Plexard
4.Moravelt
We do not installl any products. We just distribute them to architects, companies, builders, ect.
The stone can be made for any products. From laptops, countertops, "wall paper", notebooks, smart car, sinks, ect.
Dislikes: -it's hard to see what our company is -appearance -professionalism -pictures -it's not appealing
Nature
Gray, white and blacks
Blues
Red (Nothing too bright!)
below header
http://www.brevicott.example
http://www.folmaneq.example/
http://4plank.example

```html
<!DOCTYPE html>
<html lang="en">
<head>
<meta charset="utf-8">
<title>Hallvard Veneer Technology</title>
<link href="https://fonts.googleapis.com/css2?family=PT+Sans:ital,wght@0,400;0,700;1,400;1,700&family=Questrial&display=swap" rel="stylesheet">
<style>
:root{
  --bg:#1b1b1b;
  --bg-deep:#111;
  --panel:#262626;
  --line:#3a3a3a;
  --text:#9a9a9a;
  --text-light:#d8d8d8;
  --white:#fff;
  --accent:#3fb6d8;
  --brand-red:#b3262b;
  --phone:#e8b62c;
}
*{box-sizing:border-box;margin:0;padding:0}
html,body{width:1200px;height:1011px;overflow:hidden}
body{
  background:radial-gradient(ellipse at 60% 0%,#2f2f2f 0%,var(--bg) 45%,var(--bg-deep) 100%);
  font-family:"PT Sans",Verdana,sans-serif;color:var(--text);position:relative;
}
.site-header{position:absolute;left:0;top:0;width:1200px;height:140px}
.brand{
  position:absolute;left:77px;top:5px;width:205px;height:118px;background:var(--white);
  display:flex;flex-direction:column;justify-content:center;padding-left:22px;
}
.brand-row{display:flex;align-items:center;gap:10px}
.brand-mark{width:26px;height:26px;background:var(--brand-red)}
.brand-name{font-family:"PT Sans",sans-serif;font-weight:700;font-size:30px;color:var(--brand-red);line-height:1}
.brand-tag{font-weight:700;font-size:17px;color:#333;margin-top:6px}
.phone{
  position:absolute;right:82px;top:64px;font-size:21px;color:var(--white);font-style:italic;
}
.phone em{color:var(--phone);font-style:italic;font-weight:700}
.main-nav{
  position:absolute;left:77px;top:142px;width:1041px;height:34px;display:flex;align-items:center;
  font-size:15px;color:var(--text-light);
}
.main-nav a{color:inherit;text-decoration:none;margin-right:46px}
.main-nav a.active{color:var(--accent)}
.main-nav a:first-child{margin-left:34px}
.search{position:absolute;right:28px;top:7px;display:flex;align-items:center;gap:8px}
.search-field{width:172px;height:20px;background:var(--white);border-radius:2px;font-size:12px;color:#888;padding:2px 8px;display:flex;align-items:center;gap:6px}
.search-btn{width:16px;height:16px}
.gallery{position:absolute;left:77px;top:186px;width:1041px;height:373px;border:2px solid #444;background:#444}
.tile{position:absolute;overflow:hidden}
.tile .fill{position:absolute;inset:0}
.tile span{position:absolute;left:10px;bottom:6px;font-size:17px;color:var(--white);text-shadow:0 1px 2px #000}
.t1{left:0;top:0;width:263px;height:369px}
.t1 .fill{background:linear-gradient(160deg,#6b4a2c,#3a2616 55%,#8a5e36)}
.t2{left:265px;top:0;width:255px;height:369px}
.t2 .fill{background:linear-gradient(135deg,#e6e0d4 0%,#b88a5b 35%,#8d5f34 70%,#c79a6a)}
.t3{left:522px;top:0;width:256px;height:180px}
.t3 .fill{background:linear-gradient(170deg,#5b4a3c,#a08466 60%,#6a5442)}
.t4{left:780px;top:0;width:257px;height:180px}
.t4 .fill{background:linear-gradient(180deg,#d9d4c9,#a78a5e 55%,#6e5840)}
.t5{left:522px;top:182px;width:256px;height:187px}
.t5 .fill{background:linear-gradient(160deg,#d8c09a,#b3864f 50%,#7a5530)}
.t6{left:780px;top:182px;width:257px;height:187px}
.t6 .fill{background:linear-gradient(180deg,#7fa6c8 0%,#b2cbe0 35%,#a87848 60%,#6e4b2a)}
.intro{position:absolute;left:90px;top:583px;width:262px}
.section-title{font-family:"Questrial",sans-serif;font-size:25px;color:var(--text-light);font-weight:400}
.intro p{font-size:12.5px;line-height:16px;margin-top:8px}
.products{position:absolute;left:392px;top:625px;width:712px;display:flex;justify-content:space-between}
.product{width:198px}
.product .thumb{height:104px;border:2px solid #555}
.p1 .thumb{background:linear-gradient(180deg,#e9e1cc,#b79260 60%,#6f5235)}
.p2 .thumb{background:linear-gradient(180deg,#f1ead6,#caa15d 50%,#5f4426)}
.p3 .thumb{background:linear-gradient(180deg,#b7bcc2,#8d6b48 55%,#4f3a25)}
.product h3{font-family:"Questrial",sans-serif;font-weight:400;font-size:17px;color:var(--text-light);margin-top:18px}
.product p{font-size:12px;line-height:15.5px;margin-top:6px}
.site-footer{position:absolute;left:77px;top:918px;width:1041px;border-top:1px solid var(--line);padding-top:10px;font-size:12px}
.footer-links a{color:var(--text);text-decoration:none}
.footer-links .sep{margin:0 8px;color:#555}
.footer-links + .footer-links{margin-top:6px}
.copyright{margin-top:6px;font-size:11.5px}
.follow{position:absolute;right:20px;top:16px;display:flex;align-items:center;gap:24px}
.follow-label{font-family:"Questrial",sans-serif;font-size:26px;color:var(--text-light)}
.social{width:48px;height:48px;border-radius:50%;background:#3d4e66}
</style>
</head>
<body>
<header class="site-header">
  <div class="brand">
    <div class="brand-row"><div class="brand-mark"></div><div class="brand-name">Hallvard</div></div>
    <div class="brand-tag">veneer technology</div>
  </div>
  <div class="phone"><em>Toll Free:</em> 555-014-2290</div>
  <nav class="main-nav">
    <a class="active" href="#">Home</a>
    <a href="#">News</a>
    <a href="#">Products</a>
    <a href="#">Corporate Social Responsibility</a>
    <a href="#">Contact Us</a>
    <div class="search">
      <div class="search-field">
        <svg width="10" height="10" viewBox="0 0 10 10"><circle cx="4" cy="4" r="3" fill="none" stroke="#777" stroke-width="1.4"/><line x1="6.2" y1="6.2" x2="9.5" y2="9.5" stroke="#777" stroke-width="1.4"/></svg>Search
      </div>
      <svg class="search-btn" viewBox="0 0 16 16"><rect width="16" height="16" rx="2" fill="#444"/><path d="M6 4l5 4-5 4z" fill="#fff"/></svg>
    </div>
  </nav>
</header>

<section class="gallery">
  <figure class="tile t1"><div class="fill" role="img" aria-label="Wood-panelled wine cellar interior"></div><span>Lorem ipsum dolor sit amet</span></figure>
  <figure class="tile t2"><div class="fill" role="img" aria-label="Close view of stacked wood veneer planks"></div><span>Vivamus aliquam arcu sit</span></figure>
  <figure class="tile t3"><div class="fill" role="img" aria-label="Stone fireplace in a living room"></div><span>Duis molestie, augue nec</span></figure>
  <figure class="tile t4"><div class="fill" role="img" aria-label="Bright corridor with wooden wall panels"></div><span>Mauris eu nulla eu turpis</span></figure>
  <figure class="tile t5"><div class="fill" role="img" aria-label="Interior with curved wooden slat ceiling"></div><span>Quisque aliquet ipsum eget</span></figure>
  <figure class="tile t6"><div class="fill" role="img" aria-label="Building facade clad in wooden panels under blue sky"></div><span>Aenean vel libero et dolor</span></figure>
</section>

<section class="intro">
  <h2 class="section-title">Products</h2>
  <p>Solvana is a family owned importer and distributor to the tile and stone market. Products include a wide variety of Ceramic, Porcelain, Natural Stone, and Glass tile. Solvana also stocks the setting products, tools and accessories you need to get the job done right.</p>
  <p>Solvana's sales team has access to a vast assortment of industry leading specialty products. Whether a kitchen backsplash, a custom swimming pool, or a shopping mall, Solvana can provide the products that you need.</p>
</section>

<section class="products">
  <article class="product p1">
    <div class="thumb" role="img" aria-label="Lounge interior with wooden ceiling panels"></div>
    <h3>Suspendisse et sem</h3>
    <p>Morbi gravida sagittis nunc ac malesuada. Nullam vulputate, est sit amet accumsan placerat, lectus mi dapibus ligula, vitae scelerisque lorem.</p>
  </article>
  <article class="product p2">
    <div class="thumb" role="img" aria-label="Curved lattice of wooden beams"></div>
    <h3>Fusce vitae volutpat</h3>
    <p>Morbi gravida sagittis nunc ac malesuada. Nullam vulputate, est sit amet accumsan placerat, lectus mi dapibus ligula, vitae scelerisque lorem.</p>
  </article>
  <article class="product p3">
    <div class="thumb" role="img" aria-label="Hall with wood veneer wall cladding"></div>
    <h3>Sed faucibus</h3>
    <p>Morbi gravida sagittis nunc ac malesuada. Nullam vulputate, est sit amet accumsan placerat, lectus mi dapibus ligula, vitae scelerisque lorem.</p>
  </article>
</section>

<footer class="site-footer">
  <div class="footer-links"><a href="#">Home</a><span class="sep">|</span><a href="#">News</a><span class="sep">|</span><a href="#">Sonic-Paneltrim</a><span class="sep">|</span><a href="#">Stone-Veneer</a><span class="sep">|</span><a href="#">Moravelt</a><span class="sep">|</span><a href="#">Contact</a></div>
  <div class="footer-links"><a href="#">Site Map</a><span class="sep">|</span><a href="#">Privacy Policy</a><span class="sep">|</span><a href="#">Terms of services</a></div>
  <div class="copyright">Copyright © 2011 Hallvard veneer technology All Rights Reserved</div>
  <div class="follow">
    <span class="follow-label">Follow Us:</span>
    <span class="social" role="img" aria-label="Social network link"></span>
    <span class="social" role="img" aria-label="Social network link"></span>
    <span class="social" role="img" aria-label="Social network link"></span>
  </div>
</footer>
</body>
</html>
```